LWT Company Overview and Framework Training Guide

I am creating a training guide that in intended to provide sales training to independent consultants. I am working on a new Company logo and would like to match the theme, but more importantly, I want to layout the content in a modern format that keeps users engaged. The sample logo is attached and I will add more blue before it's complete.

Target Market(s)

Technology sales reps and consultants

Industry/Entity Type

Information Technology

Font styles to use
Serif
Sans Serif

Colors
3176b5
0292cd
33a6d7
0355a3
ffffff
333333
606060
1b1b1b

Requirements
Must have
• I need a company overview and a few slides that define the problem my training will help solve. I also need to show the framework and sales process, along with a demo of the software platform.
Nice to have
• Video inserts would be helpful and some slide should allow me to build out steps of the workflow.

```html
<!DOCTYPE html>
<html lang="en">
<head>
<meta charset="utf-8">
<title>LWT – New Opportunity Sales Guide</title>
<link rel="stylesheet" href="https://fonts.googleapis.com/css2?family=Montserrat:wght@400;500;600;700;800&display=swap">
<style>
  :root{
    --blue:#3176b5;
    --cyan:#0292cd;
    --sky:#33a6d7;
    --navy:#0355a3;
    --bright:#1fb8f6;
    --white:#ffffff;
    --ink:#333333;
    --grey:#606060;
    --black:#1b1b1b;
    --paper:#ffffff;
  }
  *{box-sizing:border-box;margin:0;padding:0}
  html,body{width:697px;height:1200px;overflow:hidden;background:var(--paper)}
  body{position:relative;font-family:"Montserrat",Arial,sans-serif;color:var(--ink)}
  .slide{position:absolute;width:341px;height:191px;overflow:hidden;background:var(--white);
    box-shadow:0 2px 4px rgba(0,0,0,.28)}
  .col-a{left:3px}.col-b{left:351px}
  .row-1{top:4px}.row-2{top:204px}.row-3{top:404px}.row-4{top:603px}.row-5{top:803px}.row-6{top:1002px}
  .photo{position:absolute}
  .logo{position:absolute;display:flex;align-items:center;gap:6px;color:var(--white)}
  .logo-mark{width:22px;height:22px;background:currentColor;opacity:.95}
  .logo-name{font-weight:800;font-size:15px;letter-spacing:.08em;line-height:1;
    padding-left:6px;border-left:1px solid currentColor}
  .cover-title{position:absolute;color:var(--white);font-weight:700;font-size:14px;line-height:17px;letter-spacing:.03em;white-space:nowrap}
  .center{text-align:center;left:0;right:0}
  .slide-title{position:absolute;left:16px;top:13px;font-weight:700;font-size:10.5px;color:var(--navy);letter-spacing:.04em;white-space:nowrap}
  .slide-title::before{content:"";position:absolute;left:-13px;top:-6px;width:3px;height:22px;background:var(--blue)}
  .footer{position:absolute;left:0;right:0;bottom:0;height:9px;background:var(--blue);
    display:flex;align-items:center;justify-content:flex-end;padding-right:34px;
    font-size:3.6px;color:var(--white);letter-spacing:.02em}
  .footer::before{content:"";position:absolute;left:6px;top:2px;width:5px;height:5px;background:var(--white)}
  .footer .page{position:absolute;right:6px;top:0;height:9px;width:18px;background:var(--white);
    clip-path:polygon(30% 0,100% 0,100% 100%,0 100%);color:var(--blue);font-size:4px;
    display:flex;align-items:center;justify-content:center;padding-left:3px}
  .appt{display:flex;height:100%}
  .appt-col{flex:1;display:flex;flex-direction:column;align-items:center;padding:66px 4px 0;
    color:var(--white);font-size:7.4px;line-height:9.4px;text-align:center;opacity:.95}
  .appt-col svg{margin-bottom:10px}
  .appt-heading{position:absolute;top:16px;left:0;right:0;text-align:center;color:var(--white);
    font-weight:700;font-size:11.5px;letter-spacing:.04em}
  .tile{position:absolute;color:var(--white);font-size:5.6px;line-height:6.6px;padding:8px 8px}
  .tile svg{display:block;margin-bottom:4px}
  .tile.centered{text-align:center;display:flex;flex-direction:column;align-items:center;justify-content:center;padding:4px}
  .pain-row{position:absolute;left:29px;width:266px;height:22px;display:flex;align-items:center}
  .pain-tag{width:40px;height:19px;background:var(--blue);color:var(--white);font-weight:700;font-size:5.4px;
    display:flex;align-items:center;justify-content:center;
    clip-path:polygon(15% 0,85% 0,100% 50%,85% 100%,15% 100%,0 50%);position:relative;z-index:1}
  .pain-text{flex:1;height:22px;margin-left:-6px;background:var(--white);box-shadow:0 1px 3px rgba(0,0,0,.18);
    display:flex;align-items:center;justify-content:center;color:var(--cyan);font-size:7.4px;white-space:nowrap}
</style>
</head>
<body>

<section class="slide col-a row-1">
  <div class="photo" role="img" aria-label="Blue-toned architectural photo of a modern glass building"
       style="inset:0;background:linear-gradient(125deg,#1e63a8 0%,#3a85c6 45%,#2b6fb0 70%,#0f3e78 100%)"></div>
  <div class="logo" style="left:15px;top:66px"><span class="logo-mark"></span><span class="logo-name">LWT</span></div>
  <h1 class="cover-title" style="left:12px;top:108px">NEW OPPORTUNITY<br>SALES GUIDE</h1>
</section>

<section class="slide col-b row-1" style="background:var(--blue)">
  <svg width="341" height="191" style="position:absolute;inset:0" aria-hidden="true">
    <polygon points="0,76 72,76 64,104 0,104" fill="var(--navy)"/>
    <polygon points="188,76 341,76 341,104 180,104" fill="var(--navy)"/>
    <polygon points="72,76 188,76 180,104 64,104" fill="#2e70ad"/>
  </svg>
  <div class="logo" style="left:90px;top:80px"><span class="logo-mark"></span><span class="logo-name">LWT</span></div>
  <h1 class="cover-title" style="left:70px;top:113px">NEW OPPORTUNITY<br>SALES GUIDE</h1>
</section>

<section class="slide col-a row-2">
  <div class="photo" role="img" aria-label="Blue-toned photo of a hand touching a digital network"
       style="inset:0;background:linear-gradient(135deg,#3476b8 0%,#4f8fcb 50%,#2a68a8 100%)"></div>
  <svg width="341" height="191" style="position:absolute;inset:0" aria-hidden="true">
    <polygon points="0,74 172,74 160,126 0,126" fill="var(--navy)"/>
    <polygon points="174,74 178,74 166,126 162,126" fill="var(--navy)"/>
  </svg>
  <h1 class="cover-title" style="left:6px;top:84px;text-align:right;width:142px;font-size:12.5px">NEW OPPORTUNITY<br>SALES GUIDE</h1>
  <div class="logo" style="left:176px;top:86px"><span class="logo-mark"></span><span class="logo-name">LWT</span></div>
</section>

<section class="slide col-b row-2">
  <svg width="341" height="191" style="position:absolute;inset:0" aria-hidden="true">
    <polygon points="0,64 241,64 220,110 0,110" fill="var(--cyan)"/>
    <polygon points="0,110 108,110 101,124 0,124" fill="var(--navy)"/>
  </svg>
  <h1 class="cover-title" style="left:9px;top:71px">NEW OPPORTUNITY<br>SALES GUIDE</h1>
  <div style="position:absolute;left:14px;top:112px;font-size:6.4px;font-weight:600;color:var(--white)">www.example.com</div>
  <div class="logo" style="left:242px;top:76px;color:var(--navy)"><span class="logo-mark"></span><span class="logo-name">LWT</span></div>
</section>

<section class="slide col-a row-3">
  <div class="photo" role="img" aria-label="Blue-toned photo looking up at glass skyscrapers"
       style="inset:0;background:linear-gradient(160deg,#3e80c0 0%,#2f70b0 55%,#1f5e9f 100%)"></div>
  <div class="logo" style="left:117px;top:52px"><span class="logo-mark"></span><span class="logo-name">LWT</span></div>
  <h1 class="cover-title center" style="top:100px;font-size:16px;line-height:21px">NEW OPPORTUNITY<br>SALES GUIDE</h1>
</section>

<section class="slide col-b row-3" style="background:var(--bright)">
  <div class="logo" style="left:117px;top:55px"><span class="logo-mark"></span><span class="logo-name">LWT</span></div>
  <h1 class="cover-title center" style="top:104px;font-size:16px;line-height:21px">NEW OPPORTUNITY<br>SALES GUIDE</h1>
</section>

<section class="slide col-a row-4">
  <svg width="341" height="182" viewBox="0 0 341 182" style="position:absolute;inset:0" font-family="Montserrat,Arial,sans-serif" font-size="3.4" fill="#fff" text-anchor="middle" aria-label="Sales workflow diagram">
    <g stroke="var(--navy)" stroke-width=".6" fill="none">
      <path d="M168 25v5M168 43v5M168 61v17M147 88h-12M113 88h-15M187 88h18M124 92v22M216 92v8M168 98v14M87 112h168M87 112v3M133 112v3M173 112v3M213 112v3M253 112v3M138 131v8M183 131v6M236 131v8M138 139h98"/>
    </g>
    <g fill="var(--navy)">
      <rect x="153" y="13" width="30" height="12"/><rect x="153" y="31" width="30" height="12"/><rect x="153" y="49" width="30" height="12"/>
      <rect x="76" y="82" width="22" height="11"/><rect x="113" y="84" width="22" height="8"/><rect x="205" y="84" width="22" height="8"/>
      <rect x="71" y="115" width="32" height="16"/><rect x="117" y="115" width="32" height="16"/><rect x="157" y="115" width="32" height="16"/><rect x="197" y="115" width="32" height="16"/><rect x="238" y="115" width="32" height="16"/>
      <rect x="120" y="139" width="36" height="14"/><rect x="165" y="137" width="36" height="18"/><rect x="218" y="139" width="36" height="14"/>
    </g>
    <rect x="147" y="78" width="42" height="20" fill="var(--blue)"/>
    <rect x="207" y="100" width="40" height="13" fill="#fff" stroke="#bbb" stroke-width=".5"/>
    <text x="168" y="20.5">New Lead</text><text x="168" y="38.5">Discovery</text><text x="168" y="56.5">Pain Review</text>
    <text x="168" y="87">Agree on problem</text><text x="168" y="92">and solution</text>
    <text x="87" y="89">Analysis</text><text x="124" y="89.5">Yes</text><text x="216" y="89.5">No</text>
    <text x="227" y="106" fill="#606060">Discuss next</text><text x="227" y="110" fill="#606060">steps later</text>
    <text x="87" y="124">Matrix</text><text x="133" y="124">Channel</text><text x="173" y="124">Roadmap</text><text x="213" y="124">Shortlist</text><text x="254" y="124">Finance</text>
    <text x="138" y="147">Proposal</text><text x="183" y="147">Fulfilment</text><text x="236" y="147">Ongoing</text>
  </svg>
  <div class="footer">© 2018 LWT. All rights reserved.<span class="page">7</span></div>
</section>

<section class="slide col-b row-4">
  <div class="appt">
    <div class="appt-col" style="background:#2a8ed0">
      <svg width="26" height="26" viewBox="0 0 26 26" fill="none" stroke="#fff" stroke-width="1.2"><circle cx="13" cy="13" r="9"/><circle cx="13" cy="11" r="3"/><path d="M8 19c1-3 3-4 5-4s4 1 5 4"/></svg>
      What's the purpose? UFC</div>
    <div class="appt-col" style="background:#2f9ad8">
      <svg width="26" height="26" viewBox="0 0 26 26" fill="none" stroke="#fff" stroke-width="1.2"><rect x="4" y="4" width="18" height="13"/><path d="M9 21l4-4 4 4M8 13l3-3 3 2 4-5"/></svg>
      Goals &amp; Objectives</div>
    <div class="appt-col" style="background:#3aa6de">
      <svg width="26" height="26" viewBox="0 0 26 26" fill="none" stroke="#fff" stroke-width="1.2"><circle cx="11" cy="11" r="7"/><path d="M16 16l6 6"/></svg>
      Who is the meeting with and where?</div>
    <div class="appt-col" style="background:#4cb2e4">
      <svg width="26" height="26" viewBox="0 0 26 26" fill="none" stroke="#fff" stroke-width="1.2"><rect x="3" y="4" width="20" height="18"/><path d="M3 8h20"/><circle cx="13" cy="15" r="3.5"/></svg>
      What are typical pains or issues we have solved that are similar?</div>
    <div class="appt-col" style="background:var(--blue)">
      <svg width="26" height="26" viewBox="0 0 26 26" fill="none" stroke="#fff" stroke-width="1.2"><circle cx="13" cy="13" r="10"/><circle cx="13" cy="13" r="4"/></svg>
      How to prepare? First meeting requires mostly listening skills</div>
  </div>
  <h2 class="appt-heading">YOU HAVE AN APPOINTMENT!</h2>
</section>

<section class="slide col-a row-5">
  <h2 class="slide-title">DISCOVERY CALL</h2>
  <div class="tile" style="left:17px;top:40px;width:70px;height:127px;background:#22a0d8">
    <svg width="10" height="10" viewBox="0 0 10 10" fill="none" stroke="#fff" stroke-width=".8"><path d="M5 1l4 2v3c0 2-2 3-4 4-2-1-4-2-4-4V3z"/></svg>
    Introductions
    <svg width="10" height="10" viewBox="0 0 10 10" fill="none" stroke="#fff" stroke-width=".8" style="margin-top:14px"><rect x="1" y="1" width="8" height="8"/><path d="M4 4L2.5 5.5 4 7M6 4l1.5 1.5L6 7"/></svg>
    Understanding why they need help (Why use a partner?)
  </div>
  <div class="tile" style="left:87px;top:40px;width:86px;height:65px;background:#5f5f5f">
    <svg width="10" height="10" viewBox="0 0 10 10" fill="none" stroke="#fff" stroke-width=".8"><path d="M1 9h8M2 7l2-3 2 2 3-4"/></svg>Timeline/Roadmap</div>
  <div class="tile" style="left:173px;top:40px;width:86px;height:65px;background:#0ea3df">
    <svg width="10" height="10" viewBox="0 0 10 10" fill="none" stroke="#fff" stroke-width=".8"><circle cx="4" cy="4" r="3"/><path d="M6 6l3 3"/></svg>What's the problem?<br>Pain discovery</div>
  <div class="tile" style="left:259px;top:40px;width:82px;height:65px;background:var(--blue)">
    <svg width="10" height="10" viewBox="0 0 10 10" fill="none" stroke="#fff" stroke-width=".8"><path d="M2 8l2-4 4-3-1 4-4 2z"/></svg>Success criteria</div>
  <div class="photo" role="img" aria-label="Photo of a smiling woman on a phone call"
       style="left:87px;top:105px;width:254px;height:62px;background:linear-gradient(90deg,#eef1f4 0%,#d8d4cf 55%,#9b8c80 100%)"></div>
  <div class="footer">© 2018 LWT. All rights reserved.<span class="page">8</span></div>
</section>

<section class="slide col-b row-5">
  <h2 class="slide-title">PAIN ASSESSMENT/CHALLENGES</h2>
  <div class="pain-row" style="top:41px"><span class="pain-tag">Agree on</span><span class="pain-text">Agree on this issues and priorities</span></div>
  <div class="pain-row" style="top:68px"><span class="pain-tag">Discuss</span><span class="pain-text">Discuss potential solutions</span></div>
  <div class="pain-row" style="top:95px"><span class="pain-tag">Agree on</span><span class="pain-text">Agree on best direction/strategy</span></div>
  <div class="pain-row" style="top:122px"><span class="pain-tag">Discuss</span><span class="pain-text">Discuss how to present the solution with client</span></div>
  <div class="pain-row" style="top:149px"><span class="pain-tag">Roadmap</span><span class="pain-text">Develop Roadmap and decision criteria</span></div>
  <div class="footer">© 2018 LWT. All rights reserved.<span class="page">10</span></div>
</section>

<section class="slide col-a row-6">
  <h2 class="slide-title">RESEARCH &amp; ANALYSIS</h2>
  <div class="photo" role="img" aria-label="Photo of a businessman pointing at a city skyline"
       style="left:18px;top:38px;width:102px;height:122px;background:linear-gradient(90deg,#5a6a7c 0%,#b9c4cf 60%,#e6ebef 100%)"></div>
  <div class="tile centered" style="left:124px;top:38px;width:66px;height:60px;background:#1aa0d9"><svg width="10" height="10" viewBox="0 0 10 10" fill="none" stroke="#fff" stroke-width=".8"><path d="M1 9h8M2 7l2-3 2 2 3-4"/></svg>Provider Matrix<br>&amp; Scoring</div>
  <div class="tile centered" style="left:193px;top:38px;width:66px;height:60px;background:#2a8fd0"><svg width="10" height="10" viewBox="0 0 10 10" fill="none" stroke="#fff" stroke-width=".8"><rect x="1" y="2" width="8" height="6"/><path d="M3 5h4"/></svg>Channel reviews<br>&amp; rankings</div>
  <div class="tile centered" style="left:262px;top:38px;width:66px;height:60px;background:#1aa0d9"><svg width="10" height="10" viewBox="0 0 10 10" fill="none" stroke="#fff" stroke-width=".8"><rect x="2" y="1" width="6" height="8"/><path d="M3.5 4h3M3.5 6h3"/></svg>Short Lists -<br>Evaluation<br>Results</div>
  <div class="tile centered" style="left:124px;top:101px;width:66px;height:60px;background:#1aa0d9"><svg width="10" height="10" viewBox="0 0 10 10" fill="none" stroke="#fff" stroke-width=".8"><circle cx="4" cy="4" r="3"/><path d="M6 6l3 3"/></svg>Technical scopes<br>&amp; POC</div>
  <div class="tile centered" style="left:193px;top:101px;width:66px;height:60px;background:#2a8fd0"><svg width="10" height="10" viewBox="0 0 10 10" fill="none" stroke="#fff" stroke-width=".8"><path d="M1 9h8M2 7l2-3 2 2 3-4"/></svg>Roadmap/<br>Timeline</div>
  <div class="tile centered" style="left:262px;top:101px;width:66px;height:60px;background:var(--navy)"><svg width="10" height="10" viewBox="0 0 10 10" fill="none" stroke="#fff" stroke-width=".8"><rect x="1" y="2" width="8" height="7"/><path d="M3 7V5M5 7V4M7 7V3"/></svg>Financial<br>Analysis</div>
  <div class="footer">© 2018 LWT. All rights reserved.<span class="page">11</span></div>
</section>

<section class="slide col-b row-6">
  <h2 class="slide-title">OUR VIDEO AREA</h2>
  <svg width="341" height="191" style="position:absolute;inset:0" aria-label="Laptop frame for an embedded video">
    <rect x="0" y="111" width="68" height="80" fill="#2279bd"/>
    <rect x="68" y="111" width="68" height="80" fill="#0b8fd0"/>
    <rect x="136" y="111" width="68" height="80" fill="#45bfef"/>
    <rect x="204" y="111" width="69" height="80" fill="#8fd6f5"/>
    <rect x="273" y="111" width="68" height="80" fill="#c5ebfb"/>
    <rect x="80" y="32" width="182" height="128" rx="6" fill="var(--black)"/>
    <rect x="87" y="38" width="168" height="116" fill="var(--white)"/>
    <rect x="58" y="160" width="226" height="5" rx="2" fill="#d8dadd"/>
    <rect x="58" y="164" width="226" height="2" fill="#9ea3a8"/>
  </svg>
</section>

</body>
</html>
```